Business card design needed

My company does everything from wiring up your exisiting entertainment system, to installing a complete new system for you. We can mount your plasma on the wall, install an aerial point for you, setup some surround sound in your outdoor area or install a new cinema room in your house. Any Audio or Visual requirements you may have we can provide these for you. If you want to have a party to remember at your place or just some chilled sounds by the pool, we can give you just the right size system.

Industry/Entity Type

Entertainment

Contact Information for Business Card

The Tune Crew
Colin Pemberton
e| colin@thetunecrew.com.au
w| www.thetunecrew.com.au
m| 0412 576 208

Requirements
Must have
• The logo that i have uploaded is just a starter...something similar to this but not exact or any new suggestions you have would be great too. Colour choice we are pretty easy on we did think Red and Yellow but happy to take advice, something that stands out from the rest i guess.

```html
<!DOCTYPE html>
<html lang="en">
<head>
<meta charset="utf-8">
<title>The Tune Crew — Business Card</title>
<link rel="stylesheet" href="https://fonts.googleapis.com/css2?family=Quicksand:wght@300&display=swap">
<style>
  :root {
    --card-base: #141819;
    --card-glow: #3b4041;
    --text-grey: #9ba0a0;
    --wordmark-silver: #b9c0bf;
    --divider: #4a5051;
  }
  html, body {
    margin: 0;
    padding: 0;
    width: 1200px;
    height: 741px;
    overflow: hidden;
    background: var(--card-base);
  }
  .card {
    position: relative;
    width: 1200px;
    height: 741px;
    background:
      radial-gradient(ellipse 520px 190px at 600px 0px, var(--card-glow) 0%, rgba(59,64,65,0.45) 45%, rgba(20,24,25,0) 100%),
      var(--card-base);
    font-family: "Quicksand", sans-serif;
    font-weight: 300;
    overflow: hidden;
  }
  .wordmark {
    position: absolute;
    left: 202px;
    top: 224px;
    width: 323px;
    height: 145px;
    display: flex;
    align-items: center;
    justify-content: center;
    color: var(--wordmark-silver);
    font-size: 42px;
    letter-spacing: 0.5px;
    white-space: nowrap;
  }
  .divider {
    position: absolute;
    left: 599px;
    top: 171px;
    width: 1px;
    height: 322px;
    background: var(--divider);
  }
  .contact {
    position: absolute;
    left: 656px;
    top: 219px;
    margin: 0;
    padding: 0;
    list-style: none;
    color: var(--text-grey);
    font-size: 20px;
    line-height: 34.2px;
    letter-spacing: -0.2px;
  }
  .contact li { white-space: nowrap; }
  .contact .company { text-transform: uppercase; }
</style>
</head>
<body>
  <div class="card">
    <div class="wordmark">The Tune Crew</div>
    <div class="divider"></div>
    <ul class="contact">
      <li class="company">The Tune Crew</li>
      <li class="name">Colin Pemberton</li>
      <li class="email">colin@thetunecrew.com.au</li>
      <li class="web">www.thetunecrew.com.au</li>
      <li class="phone">0412 576 208</li>
    </ul>
  </div>
</body>
</html>
```